Professional and creatice Life Coach - Business Card design

I just relaunched my website and now i a need a correspoonding business card for my task as life coach. My website is www.tbalrond.com as reference. The compass is kind of a symbol for my work, as I help people navigate through their challenging phases in life. The business card should be colorful, but not too playful as I also adress business people. So it sould be creative, but professional (also to suport my other business as Management Consultant)

Target Market(s)

People who want to get teir problems resolved, in business, partnership and other personal realms

Industry/Entity Type

Life Coaching

Contact Information for Business Card

Front side should include Name, Phone number, Email, Website and address

Font styles to use
Sans Serif

Colors
add136

Requirements
Must have
• "Mag. Leopold Brantner" -> Name
"Energetische Praxis" -> Jobtitle (describing my profession as life coach)
colours and style should match my website www.tbalrond.com
Nice to have
• a compass as a symbol

```html
<!DOCTYPE html>
<html lang="de">
<head>
<meta charset="utf-8">
<title>Leopold Brantner – Visitenkarte</title>
<link rel="stylesheet" href="https://fonts.googleapis.com/css2?family=Roboto:wght@400;500&family=Saira+Semi+Condensed:wght@700&display=swap">
<style>
  :root {
    --backdrop: #3a3a3a;
    --card: #1f1f21;
    --card-edge: #2a2a2c;
    --lime: #add136;
    --ink: #111111;
    --paper-text: #e6e6e6;
    --emboss: #4a4a4d;
  }
  * { margin: 0; padding: 0; box-sizing: border-box; }
  html, body { width: 799px; height: 1200px; overflow: hidden; }
  body {
    background: var(--backdrop);
    font-family: "Roboto", sans-serif;
    position: relative;
  }
  .card {
    position: absolute;
    left: 90px;
    width: 620px;
    height: 354px;
    background: var(--card);
    border: 1px solid var(--card-edge);
    border-radius: 3px;
    box-shadow: 0 14px 30px rgba(0,0,0,0.45);
    overflow: hidden;
  }
  .card--front { top: 128px; }
  .card--back { top: 720px; }

  .brand-mark {
    position: absolute;
    display: flex;
    align-items: center;
    gap: 12px;
    font-family: "Saira Semi Condensed", sans-serif;
    font-weight: 700;
  }
  .card--front .brand-mark {
    left: 50%; top: 50%;
    transform: translate(-50%, -50%);
    font-size: 44px;
    color: var(--emboss);
  }
  .brand-mark__dot {
    width: 22px; height: 22px;
    border-radius: 50%;
    border: 3px solid currentColor;
  }
  .card--back .brand-mark {
    left: 340px; top: 48px;
    font-size: 28px;
    color: var(--lime);
    gap: 9px;
  }
  .card--back .brand-mark__dot { width: 16px; height: 16px; border-width: 2px; }

  .info-band {
    position: absolute;
    left: 0; right: 0;
    top: 138px;
    height: 138px;
    background: var(--lime);
    color: var(--ink);
  }
  .identity {
    position: absolute;
    left: 38px; top: 26px;
  }
  .identity__name {
    font-family: "Saira Semi Condensed", sans-serif;
    font-weight: 700;
    font-size: 26px;
    line-height: 1.1;
  }
  .identity__role {
    font-size: 17px;
    margin-top: 2px;
  }
  .contacts {
    position: absolute;
    left: 346px; top: 30px;
    list-style: none;
    font-size: 17px;
    line-height: 26px;
  }
  .contacts li { display: flex; align-items: center; gap: 12px; }
  .contacts svg { width: 15px; height: 15px; fill: var(--ink); flex: none; }
  .address {
    position: absolute;
    left: 38px; top: 298px;
    font-size: 17px;
    color: var(--paper-text);
  }
</style>
</head>
<body>
  <section class="card card--front" aria-label="Vorderseite">
    <div class="brand-mark"><span class="brand-mark__dot"></span>tbalrond</div>
  </section>

  <section class="card card--back" aria-label="Rückseite">
    <div class="brand-mark"><span class="brand-mark__dot"></span>tbalrond</div>
    <div class="info-band">
      <div class="identity">
        <h1 class="identity__name">Mag. Leopold Brantner</h1>
        <p class="identity__role">Energetische Praxis</p>
      </div>
      <ul class="contacts">
        <li>
          <svg viewBox="0 0 16 16" aria-hidden="true"><path d="M3 2h3l1.5 3.5-2 1.3a8 8 0 0 0 3.7 3.7l1.3-2L14 10v3a1 1 0 0 1-1 1A11 11 0 0 1 2 3a1 1 0 0 1 1-1z"/></svg>
          +43 664 3817462
        </li>
        <li>
          <svg viewBox="0 0 16 16" aria-hidden="true"><path d="M1 3h14v10H1z M2 4l6 5 6-5" fill="none" stroke="#111" stroke-width="1.6"/></svg>
          leopold@brantner.one
        </li>
        <li>
          <svg viewBox="0 0 16 16" aria-hidden="true"><circle cx="8" cy="8" r="6.5" fill="none" stroke="#111" stroke-width="1.5"/><path d="M1.5 8h13M8 1.5c-3 3.5-3 9.5 0 13M8 1.5c3 3.5 3 9.5 0 13" fill="none" stroke="#111" stroke-width="1.2"/></svg>
          www.tbalrond.com
        </li>
      </ul>
    </div>
    <p class="address">Ahornweg 14, 5400 Hallein, Österreich</p>
  </section>
</body>
</html>
```